Skin Care business card for esthetician that is home based

I need a business card for my esthetician business. I would like to use a picture provided.
I want the picture #1 that I have provided to be as the main background with my title and the moto underneath in smaller lettering. Below that as a seperate thing I would like my full name and underneath in small letters to say "esthetician".
As a seperate paragraph I would like my address then phone number, email and my website that I have provided in the business card details.
On the back side I would like my second picture to be small and in the top left corner and then have the "nice to haves" details to be at the center bottom of the card.
Target Market(s)
mosty women between 18 and 60 years old
Industry/Entity Type
Skin Care
Contact Information for Business Card
Velvet Bloom Skin Care - Main Title
Guiding you to radiance! - motto
Marisol Teodora Vinchek -
Phone: 314.827.5093
7382 SW 9th Avenue
Oakvale WA 98472
oakvaleskincare@mailhaven.example
www.oakvaleskincare.example
Must have
- Picure I provided or other similar photo.
Nice to have
- On the back side:
Guiding you to radiance!
www.oakvaleskincare.example

```html
<!DOCTYPE html>
<html lang="en">
<head>
<meta charset="utf-8">
<title>Velvet Bloom Skin Care – Business Card</title>
<link href="https://fonts.googleapis.com/css2?family=Playball&family=Playfair+Display:wght@400&family=Open+Sans:wght@400&display=swap" rel="stylesheet">
<style>
  :root {
    --stage: #e6e3e1;
    --card-light: #fbf3f0;
    --card-shade: #ecdfdb;
    --ink: #2b2523;
    --ink-soft: #3d3431;
    --photo-warm: #c9a089;
    --photo-deep: #7a5542;
    --photo-pale: #efe2da;
  }
  * { margin: 0; padding: 0; box-sizing: border-box; }
  html, body { width: 1200px; height: 900px; overflow: hidden; }
  body { background: var(--stage); position: relative; font-family: "Open Sans", sans-serif; color: var(--ink); }

  .card {
    position: absolute;
    width: 620px;
    height: 354px;
    border-radius: 22px;
    overflow: hidden;
    background: linear-gradient(135deg, var(--card-light) 0%, var(--card-light) 45%, var(--card-shade) 100%);
    box-shadow: 0 10px 24px rgba(0,0,0,.18);
  }

  /* Back side */
  .card-back { left: 150px; top: 46px; text-align: center; }
  .portrait {
    width: 104px; height: 104px; border-radius: 50%;
    margin: 26px auto 0;
    background: radial-gradient(circle at 50% 40%, #e9d3b9 0%, #cdb08e 55%, #b59372 100%);
  }
  .back-motto {
    font-family: "Playball", cursive;
    font-weight: 400;
    font-size: 54px; line-height: 1.02;
    color: var(--ink-soft);
    margin-top: 18px;
  }
  .back-rule { width: 90px; height: 1px; background: var(--ink-soft); margin: 14px auto 10px; }
  .back-web { font-family: "Playfair Display", serif; font-size: 19px; letter-spacing: .3px; }

  /* Front side */
  .card-front { left: 430px; top: 500px; }
  .hero-photo {
    position: absolute; inset: 0;
    background:
      linear-gradient(90deg, rgba(251,243,240,0) 0%, rgba(251,243,240,0) 48%, rgba(251,243,240,.85) 64%, var(--card-light) 74%),
      radial-gradient(ellipse at 34% 38%, var(--photo-pale) 0%, var(--photo-warm) 38%, var(--photo-deep) 80%);
  }
  .front-info {
    position: absolute; right: 18px; top: 20px; width: 260px;
    text-align: center;
  }
  .brand { font-family: "Playfair Display", serif; font-weight: 400; font-size: 34px; line-height: 1.05; }
  .front-motto { font-size: 11px; margin-top: 3px; }
  .person { font-family: "Playfair Display", serif; font-weight: 400; font-size: 21px; line-height: 1.15; margin-top: 14px; }
  .role { font-size: 12px; margin-top: 2px; }
  .front-rule { width: 54px; height: 2px; background: var(--ink); margin: 10px auto 12px; }
  .address, .contact { font-size: 13px; line-height: 1.35; }
  .contact { margin-top: 12px; }
</style>
</head>
<body>

<section class="card card-back" aria-label="Business card back">
  <div class="portrait" role="img" aria-label="Small portrait photo of the esthetician"></div>
  <p class="back-motto">Guiding you<br>to radiance!</p>
  <div class="back-rule"></div>
  <p class="back-web">www.oakvaleskincare.example</p>
</section>

<section class="card card-front" aria-label="Business card front">
  <div class="hero-photo" role="img" aria-label="Photo of a woman receiving a facial treatment at a spa"></div>
  <div class="front-info">
    <h1 class="brand">Velvet Bloom<br>Skin Care</h1>
    <p class="front-motto">Guiding you to radiance!</p>
    <h2 class="person">Marisol<br>Teodora Vinchek</h2>
    <p class="role">esthetician</p>
    <div class="front-rule"></div>
    <p class="address">7382 SW 9th Avenue<br>Oakvale WA 98472</p>
    <p class="contact">314 827 5093<br>oakvaleskincare@mailhaven.example<br>www.oakvaleskincare.example</p>
  </div>
</section>

</body>
</html>
```